Attorney Business Card

I need a business card that looks professional yet modern. I am an Attorney. , I need a professional yet modern business card for my law practice. My logo and information have been uploaded. , I need a business card that looks professional yet modern. I am an Attorney. , I need a professional yet modern business card for my law practice. My logo and information have been uploaded.

Industry/Entity Type

Business

Requirements
Must have
• My logo which has been uploaded , my logo , My logo which has been uploaded , my logo

```html
<!DOCTYPE html>
<html lang="en">
<head>
<meta charset="utf-8">
<title>Marlowe Law Firm – Business Card</title>
<link rel="stylesheet" href="https://fonts.googleapis.com/css2?family=Cinzel:wght@400;600&display=swap">
<style>
  :root {
    --brand-blue: #29a8e0;
    --text-grey: #8a8a8a;
    --card-white: #ffffff;
    --page-bg: #e9eaec;
    --shadow: rgba(0, 0, 0, 0.18);
  }
  * { box-sizing: border-box; margin: 0; padding: 0; }
  html, body { width: 1200px; height: 960px; overflow: hidden; }
  body {
    background: var(--page-bg);
    font-family: "Cinzel", "Times New Roman", serif;
    position: relative;
  }
  .card {
    position: absolute;
    left: 250px;
    width: 700px;
    height: 400px;
    border-radius: 22px;
    box-shadow: 0 6px 18px var(--shadow);
    overflow: hidden;
  }
  .card--front { top: 40px; background: var(--card-white); }
  .card--back { top: 520px; background: var(--brand-blue); }

  .attorney {
    position: absolute; left: 42px; top: 46px;
    color: var(--brand-blue); font-size: 27px; line-height: 1.2;
  }
  .address {
    position: absolute; right: 42px; top: 40px; text-align: right;
    color: var(--text-grey); font-size: 17px; line-height: 1.3;
  }
  .contact {
    position: absolute; color: var(--text-grey);
    font-size: 15px; line-height: 1.4; letter-spacing: 0.5px;
  }
  .contact--phones { left: 58px; top: 196px; }
  .contact--online { right: 40px; top: 168px; width: 240px; text-align: center; }

  .firm-dot {
    position: absolute; left: 300px; top: 108px;
    width: 100px; height: 100px; border-radius: 50%;
    border: 4px solid var(--brand-blue);
  }
  .firm-name {
    position: absolute; left: 0; right: 0; top: 252px;
    text-align: center; color: var(--brand-blue);
    font-size: 40px; font-weight: 600; letter-spacing: 2px;
  }
  .website {
    position: absolute; left: 0; right: 0; top: 336px; text-align: center;
    color: var(--text-grey); font-size: 18px; letter-spacing: 1px;
  }

  .back-dot {
    position: absolute; left: 260px; top: 50px;
    width: 180px; height: 180px; border-radius: 50%;
    background: var(--card-white);
  }
  .back-name {
    position: absolute; left: 0; right: 0; top: 268px;
    text-align: center; color: var(--card-white);
    font-size: 36px; font-weight: 600; letter-spacing: 2px;
  }
</style>
</head>
<body>
  <section class="card card--front" aria-label="Business card front">
    <p class="attorney">Daniel Marlowe, Esq.<br>Attorney at Law</p>
    <p class="address">2180 Cedar Crest Ave<br>Suite 400<br>Fairview, CA 90317</p>
    <p class="contact contact--phones">Office: 555.210.4400<br>Mobile: 555.318.2270</p>
    <p class="contact contact--online">daniel@marlowefirm.com<br>Fax: 555.210.4488</p>
    <div class="firm-dot" aria-hidden="true"></div>
    <p class="firm-name">Marlowe Law Firm</p>
    <p class="website">www.marlowefirm.com</p>
  </section>

  <section class="card card--back" aria-label="Business card back">
    <div class="back-dot" aria-hidden="true"></div>
    <p class="back-name">Marlowe Law Firm</p>
  </section>
</body>
</html>
```